New Business Card Design Project

Hi there

Could you please make a design that is soft and appealing to people who would purchase gemstones, buy healing jewellery, seek counselling, may seek energy healing and/or learn English. Essentially I'm looking for something with a soft human design. Please incorporate the logo and select font that can be easily read and softer images in the background - but not too busy. I would like it double sided as well.

Optional: Elements could include gemstones, feathers, plants and images that are happy and calming.

Target Market(s)

People into alternative health, those from non-English speaking backgrounds, businesses

Contact Information for Business Card

Leo Marsdon
Mobile: 0412 586 239, Facebook and Instagram Logos,
ABN: 51 742 118 603 (Australian Business Number - small at the bottom)

Requirements
Must have
• My project must have:
- Tranquil Harbor logo
- Symbols that represent the 4 main services: 1. Gemstones/jewellery, 2. counselling, 3. meditation/energy healing, 4. education
Nice to have
• Clear and easy to read.

```html
<!DOCTYPE html>
<html lang="en">
<head>
<meta charset="utf-8">
<title>Tranquil Harbor – Business Card</title>
<link href="https://fonts.googleapis.com/css2?family=Exo+2:wght@600;700&display=swap" rel="stylesheet">
<style>
  :root {
    --backdrop: #757575;
    --card-white: #ffffff;
    --orange: #ee8520;
    --amber: #f5a817;
    --yellow: #f8c30d;
    --brand-green: #6aa83c;
    --brand-teal: #3db3a8;
    --leaf: #b5ad2a;
    --text-light: #ffffff;
  }
  html, body {
    margin: 0;
    padding: 0;
    width: 1113px;
    height: 1200px;
    overflow: hidden;
    background: var(--backdrop);
    font-family: "Exo 2", Arial, sans-serif;
  }
  .card {
    position: absolute;
    left: 292px;
    width: 546px;
    height: 333px;
    background: var(--card-white);
    overflow: hidden;
  }
  .card--front { top: 196px; }
  .card--back { top: 589px; }
  .card__shape {
    position: absolute;
    inset: 0;
    width: 100%;
    height: 100%;
  }
  .tree-art {
    position: absolute;
    border-radius: 40% 60% 30% 50%;
    background: linear-gradient(160deg, var(--leaf) 0%, var(--leaf) 45%, var(--amber) 100%);
  }
  .card--front .tree-art { left: 222px; top: 58px; width: 68px; height: 120px; }
  .card--back .tree-art { left: 404px; top: 58px; width: 66px; height: 120px; }

  .brand {
    position: absolute;
    text-align: center;
    color: var(--brand-green);
    font-weight: 600;
    line-height: 1;
    letter-spacing: 1px;
  }
  .brand__mark {
    display: block;
    margin: 0 auto;
    border: 3px solid var(--brand-teal);
    border-radius: 50%;
  }
  .card--front .brand { left: 29px; top: 86px; width: 200px; font-size: 28px; }
  .card--front .brand__mark { width: 58px; height: 58px; margin-bottom: 10px; }
  .card--back .brand { left: 117px; top: 78px; width: 260px; font-size: 38px; }
  .card--back .brand__mark { width: 78px; height: 78px; margin-bottom: 14px; }

  .contact {
    position: absolute;
    left: 317px;
    top: 0;
    color: var(--text-light);
  }
  .contact__name {
    position: absolute;
    top: 48px;
    margin: 0;
    font-size: 26px;
    font-weight: 700;
    white-space: nowrap;
    letter-spacing: 0.5px;
    padding-bottom: 4px;
  }
  .contact__rule {
    position: absolute;
    top: 84px;
    width: 152px;
    height: 1.5px;
    background: var(--text-light);
  }
  .contact__row {
    position: absolute;
    display: flex;
    align-items: center;
    gap: 10px;
    font-size: 16px;
    font-weight: 600;
    white-space: nowrap;
    letter-spacing: 0.5px;
  }
  .contact__row--phone { top: 110px; }
  .contact__row--social { top: 156px; }
  .contact__row--handle { top: 200px; }
  .icon { width: 21px; height: 21px; flex: none; }

  .abn {
    position: absolute;
    left: 0;
    top: 270px;
    width: 546px;
    height: 43px;
    background: linear-gradient(90deg, var(--orange) 0%, var(--orange) 55%, var(--yellow) 100%);
    color: var(--text-light);
  }
  .abn__rule {
    position: absolute;
    top: 21px;
    height: 1.5px;
    background: var(--text-light);
  }
  .abn__rule--left { left: 28px; width: 116px; }
  .abn__rule--right { left: 400px; width: 117px; }
  .abn__text {
    position: absolute;
    left: 0;
    width: 546px;
    top: 11px;
    text-align: center;
    font-size: 19px;
    font-weight: 700;
    letter-spacing: 0.5px;
  }
</style>
</head>
<body>

<section class="card card--front" aria-label="Business card front">
  <svg class="card__shape" viewBox="0 0 546 333" aria-hidden="true">
    <defs>
      <linearGradient id="front-fill" x1="0" y1="0" x2="0" y2="1">
        <stop offset="0" stop-color="#f8c30d"/>
        <stop offset="0.6" stop-color="#f0901d"/>
        <stop offset="1" stop-color="#ee8520"/>
      </linearGradient>
    </defs>
    <path d="M287 0 H546 V333 H279 C281 310 283 290 282 270 C283 220 292 190 290 150 C288 110 280 70 282 40 C283 20 285 8 287 0 Z" fill="url(#front-fill)"/>
  </svg>
  <div class="tree-art" role="img" aria-label="Illustration of a slender tree with olive leaves growing from the orange curve"></div>

  <div class="brand">
    <span class="brand__mark" aria-hidden="true"></span>
    TRANQUIL<br>HARBOR
  </div>

  <div class="contact">
    <h1 class="contact__name">LEO MARSDON</h1>
    <div class="contact__rule"></div>
    <div class="contact__row contact__row--phone">
      <svg class="icon" viewBox="0 0 24 24" aria-hidden="true">
        <circle cx="12" cy="12" r="11" fill="#fff"/>
        <path d="M9 6c-1 0-2 1-2 2 0 5 4 10 9 10 1 0 2-1 2-2l-2-2-2 1c-2-1-3-3-4-5l1-2z" fill="#f29a1c"/>
      </svg>
      <span>0412 586 239</span>
    </div>
    <div class="contact__row contact__row--social">
      <svg class="icon" viewBox="0 0 24 24" aria-hidden="true">
        <rect x="2" y="2" width="20" height="20" rx="3" fill="none" stroke="#fff" stroke-width="2.5"/>
      </svg>
      <span>tranquilharbor.au</span>
    </div>
    <div class="contact__row contact__row--handle">
      <svg class="icon" viewBox="0 0 24 24" aria-hidden="true">
        <circle cx="12" cy="12" r="10" fill="none" stroke="#fff" stroke-width="2.5"/>
      </svg>
      <span>@tranquilharbor</span>
    </div>
  </div>

  <div class="abn">
    <div class="abn__rule abn__rule--left"></div>
    <div class="abn__text">ABN: 51 742 118 603</div>
    <div class="abn__rule abn__rule--right"></div>
  </div>
</section>

<section class="card card--back" aria-label="Business card back">
  <svg class="card__shape" viewBox="0 0 546 333" aria-hidden="true">
    <defs>
      <linearGradient id="back-fill" x1="0" y1="0" x2="0" y2="1">
        <stop offset="0" stop-color="#f8c30d"/>
        <stop offset="0.6" stop-color="#f0901d"/>
        <stop offset="1" stop-color="#ee8520"/>
      </linearGradient>
    </defs>
    <path d="M469 0 H546 V333 H461 C465 300 467 270 466 240 C466 200 473 180 471 140 C469 100 462 70 464 40 C465 20 467 8 469 0 Z" fill="url(#back-fill)"/>
  </svg>
  <div class="tree-art" role="img" aria-label="Illustration of a slender tree with olive leaves growing from the orange curve"></div>

  <div class="brand">
    <span class="brand__mark" aria-hidden="true"></span>
    TRANQUIL<br>HARBOR
  </div>
</section>

</body>
</html>
```